Business Card Design Project

We need a Business Card for an Mechanical Engineering firm in Singapore. The design should be Modern & Technical looking, yet eye catching.

Our company deals in Cutting Tools & Machine Accessories for the Manufacturing Industries such as Oil & Gas, Aero Space, etc... For more information on our Company, you can either email me or view our website www.valtrion.com.sg.

We are trying to revamp our image to give our consumers a fresh new perspective to our company, so we welcome all ideas.

Industry/Entity Type

Business

Requirements
Must have
• Must incorporate New Company Logo into the card as shown in Uploaded file.

```html
<!DOCTYPE html>
<html lang="en">
<head>
<meta charset="utf-8">
<title>Valtrion Tools – Business Card</title>
<link rel="stylesheet" href="https://fonts.googleapis.com/css2?family=Kalam:wght@400&display=swap">
<style>
  :root {
    --maroon: #7e0013;
    --maroon-text: #8a1628;
    --edge: #111111;
    --paper: #ffffff;
    --ink-light: #ffffff;
  }
  html, body {
    margin: 0;
    padding: 0;
    overflow: hidden;
    background: var(--paper);
  }
  .card {
    position: relative;
    width: 1200px;
    height: 686px;
    overflow: hidden;
    background: var(--paper);
    font-family: "Kalam", cursive;
  }
  .card__sweep {
    position: absolute;
    inset: 0;
    width: 1200px;
    height: 686px;
  }
  .sweep__edge { fill: var(--edge); }
  .sweep__band { fill: var(--maroon); }

  .brand {
    position: absolute;
    left: 6px;
    top: 40px;
    display: flex;
    flex-direction: column;
    align-items: center;
  }
  .brand__dot {
    width: 84px;
    height: 84px;
    border-radius: 50%;
    background: var(--maroon);
  }
  .brand__name {
    margin-top: 6px;
    font-size: 46px;
    line-height: 1;
    color: var(--maroon);
    letter-spacing: 1px;
    white-space: nowrap;
  }

  .holder {
    position: absolute;
    left: 60px;
    top: 335px;
    color: var(--maroon-text);
    font-size: 41px;
    line-height: 57px;
  }
  .holder__name { margin: 0; }
  .holder__role { margin: 0 0 0 48px; }

  .contact {
    position: absolute;
    left: 771px;
    top: 438px;
    color: var(--ink-light);
    font-size: 27px;
    line-height: 34px;
    letter-spacing: 0.5px;
  }
  .contact__address { margin: 0 0 34px; font-style: normal; }
  .contact__lines { margin: 0; padding: 0; list-style: none; }
  .contact__label { display: inline-block; min-width: 70px; }
</style>
</head>
<body>
  <main class="card">
    <svg class="card__sweep" viewBox="0 0 1200 686" aria-hidden="true">
      <path class="sweep__edge" transform="translate(-5,-9)"
            d="M1042,0 C1062,200 962,330 760,412 C560,492 220,542 0,626 L0,700 L1210,700 L1210,0 Z"/>
      <path class="sweep__band"
            d="M1042,0 C1062,200 962,330 760,412 C560,492 220,542 0,626 L0,686 L1200,686 L1200,0 Z"/>
    </svg>

    <header class="brand">
      <span class="brand__dot"></span>
      <span class="brand__name">VALTRION TOOLS</span>
    </header>

    <section class="holder">
      <p class="holder__name">Marianne</p>
      <p class="holder__role">Manager</p>
    </section>

    <section class="contact">
      <address class="contact__address">
        27 Kestrel Crescent #03-12,<br>
        Kestrel Industrial Hub,<br>
        Singapore 609874
      </address>
      <ul class="contact__lines">
        <li><span class="contact__label">Tel:</span> 65-63921470</li>
        <li>Fax: 65-63921471</li>
        <li>Email: valtrion@valtrion.com.sg</li>
      </ul>
    </section>
  </main>
</body>
</html>
```